Hello,
Corinne Haskett Equestrian needs a business card. We are a high performance show jumping stables based at Willowmere Reserve in morningotn. We pride ourselves on producing high quality show jumping horses and competing our stock at a high level. My business card need to have my logo on it, and i would like it to have a classic design with a modern touch. I would like it to have quite a natural feel about it. It needs to be in a font which is easy to read as I spend a lot of time competing internationally and overseas, and i need to be able to give it out to breeders and contacts where English isnt their first language. I will need it to include the following details:
-Corinne Haskett Equestrian
-Based at Willowmere Reserve Mornington
-Address: 17 Tremont Lane Mornington Victoria 3931
-Mobile number: 0412605948
- website: www.corinnehaskettequestrian.example
Target Market(s)
For business adults who english may not be their first language
Industry/Entity Type
Business

```html
<!DOCTYPE html>
<html lang="en">
<head>
<meta charset="utf-8">
<title>Corinne Haskett Equestrian – Business Card</title>
<link rel="stylesheet" href="https://fonts.googleapis.com/css2?family=Cinzel:wght@400&family=Open+Sans:wght@400;600&display=swap">
<style>
  :root {
    --bg: #e9e9e9;
    --card: #ffffff;
    --rust: #c4672b;
    --ink: #3a3a3a;
    --slate: #4a4a4a;
    --muted: #6a6a6a;
  }
  * { margin: 0; padding: 0; box-sizing: border-box; }
  html, body { width: 1200px; height: 885px; overflow: hidden; }
  body {
    background: var(--bg);
    font-family: "Open Sans", Arial, sans-serif;
    position: relative;
  }
  .card {
    position: absolute;
    width: 540px;
    height: 310px;
    background: var(--card);
    box-shadow: 0 2px 6px rgba(0,0,0,0.12);
    overflow: hidden;
  }
  .card--front { left: 40px; top: 287px; }
  .card--back  { left: 620px; top: 287px; }

  .brand {
    font-family: "Cinzel", Georgia, serif;
    font-weight: 400;
    color: var(--slate);
    letter-spacing: 0.04em;
    white-space: nowrap;
  }
  .brand-dot {
    display: block;
    border-radius: 50%;
    background: var(--rust);
  }

  /* Front */
  .front-logo {
    position: absolute;
    left: 0; right: 0; top: 108px;
    display: flex; flex-direction: column; align-items: center; gap: 16px;
  }
  .front-logo .brand-dot { width: 34px; height: 34px; }
  .front-logo .brand { font-size: 24px; }

  /* Back */
  .back-logo {
    position: absolute; left: 28px; top: 58px;
    display: flex; align-items: center; gap: 10px;
  }
  .back-logo .brand-dot { width: 20px; height: 20px; }
  .back-logo .brand { font-size: 14px; }

  .name-bar {
    position: absolute; left: 0; top: 110px;
    width: 245px; height: 40px;
    background: var(--rust);
    padding: 5px 0 0 28px;
    color: #fff;
  }
  .name-bar .person { font-size: 14px; font-weight: 600; letter-spacing: 0.04em; line-height: 1.2; }
  .name-bar .role { font-size: 9px; letter-spacing: 0.12em; line-height: 1.3; }

  .rule-line {
    position: absolute; left: 245px; right: 0; top: 110px; height: 5px;
    background: var(--rust);
  }
  .stripe-block { position: absolute; left: 210px; top: 84px; }
  .social-pendants { position: absolute; right: 0; top: 0; }

  .contact-list {
    position: absolute; list-style: none;
    font-size: 11px; color: var(--ink);
    white-space: nowrap;
  }
  .contact-list--left { left: 60px; top: 176px; }
  .contact-list--right { left: 272px; top: 176px; }
  .contact-list li {
    display: flex; align-items: flex-start; gap: 9px;
    margin-bottom: 9px; line-height: 16px;
  }
  .icon { flex: none; width: 16px; height: 16px; }
</style>
</head>
<body>

<section class="card card--front" aria-label="Card front">
  <div class="front-logo">
    <span class="brand-dot" aria-hidden="true"></span>
    <span class="brand">Corinne Haskett Equestrian</span>
  </div>
</section>

<section class="card card--back" aria-label="Card back">
  <svg class="social-pendants" width="130" height="100" viewBox="0 0 130 100" aria-hidden="true">
    <g stroke="#444" stroke-width="1.5">
      <line x1="30" y1="0" x2="30" y2="30"/>
      <line x1="62" y1="0" x2="62" y2="48"/>
      <line x1="94" y1="0" x2="94" y2="66"/>
    </g>
    <g fill="#3d3d3d">
      <circle cx="30" cy="40" r="11"/>
      <circle cx="62" cy="58" r="11"/>
      <circle cx="94" cy="76" r="11"/>
    </g>
  </svg>

  <div class="back-logo">
    <span class="brand-dot" aria-hidden="true"></span>
    <span class="brand">Corinne Haskett Equestrian</span>
  </div>

  <svg class="stripe-block" width="110" height="28" viewBox="0 0 110 28" aria-hidden="true">
    <polygon points="20,0 110,0 90,26 0,26" fill="#3d3d3d"/>
    <g stroke="#fff" stroke-width="3">
      <line x1="45" y1="0" x2="25" y2="26"/>
      <line x1="65" y1="0" x2="45" y2="26"/>
      <line x1="85" y1="0" x2="65" y2="26"/>
    </g>
  </svg>

  <div class="name-bar">
    <p class="person">CORINNE HASKETT</p>
    <p class="role">GENERAL MANAGER</p>
  </div>
  <div class="rule-line" aria-hidden="true"></div>

  <ul class="contact-list contact-list--left">
    <li>
      <svg class="icon" viewBox="0 0 16 16" aria-hidden="true"><circle cx="8" cy="8" r="8" fill="var(--rust)"/><path d="M5.5 4.2l1.4-.3.8 2-1 .7c.4 1 1.1 1.8 2.1 2.2l.7-1 2 .8-.3 1.4c-3.2.2-5.9-2.6-5.7-5.8z" fill="#fff"/></svg>
      <span>0412 605 948</span>
    </li>
    <li>
      <svg class="icon" viewBox="0 0 16 16" aria-hidden="true"><circle cx="8" cy="8" r="8" fill="var(--rust)"/><rect x="5.5" y="3.5" width="5" height="9" rx="1" fill="#fff"/><rect x="6.3" y="4.6" width="3.4" height="5.6" fill="var(--rust)"/></svg>
      <span>0412 605 948</span>
    </li>
    <li>
      <svg class="icon" viewBox="0 0 16 16" aria-hidden="true"><circle cx="8" cy="8" r="8" fill="var(--rust)"/><path d="M8 3.5a3 3 0 0 0-3 3c0 2.2 3 5.8 3 5.8s3-3.6 3-5.8a3 3 0 0 0-3-3z" fill="#fff"/><circle cx="8" cy="6.5" r="1.1" fill="var(--rust)"/></svg>
      <span>Based at Willowmere Reserve<br>17 Tremont Lane<br>Mornington VIC 3931</span>
    </li>
  </ul>

  <ul class="contact-list contact-list--right">
    <li>
      <svg class="icon" viewBox="0 0 16 16" aria-hidden="true"><circle cx="8" cy="8" r="8" fill="var(--rust)"/><rect x="4" y="5" width="8" height="6" fill="#fff"/><path d="M4 5l4 3.2L12 5" fill="none" stroke="var(--rust)" stroke-width="0.9"/></svg>
      <span>hello@corinnehaskett.example</span>
    </li>
    <li>
      <svg class="icon" viewBox="0 0 16 16" aria-hidden="true"><circle cx="8" cy="8" r="8" fill="var(--rust)"/><g fill="none" stroke="#fff" stroke-width="0.9"><circle cx="8" cy="8" r="4"/><ellipse cx="8" cy="8" rx="1.7" ry="4"/><line x1="4" y1="8" x2="12" y2="8"/></g></svg>
      <span>www.corinnehaskettequestrian.example</span>
    </li>
  </ul>
</section>

</body>
</html>
```